Business Card Design Project

We're an orthopaedic office, and our colors are blue white and balck. Dealing with physicians and healthcare execs, I'd like this card to have a classy, yet overpowering wow factor.

Here are a couple of cards I like that are close to what I'm looking for:
http://www.plumvantia.com/design/671583
http://www.plumvantia.com/design/514515

```html
<!DOCTYPE html>
<html lang="en">
<head>
<meta charset="utf-8">
<title>Crestline Orthopaedic – Business Card</title>
<link rel="stylesheet" href="https://fonts.googleapis.com/css2?family=Arimo:wght@400;700&display=swap">
<style>
  :root {
    --backdrop: #e4e5e7;
    --card-blue-light: #146096;
    --card-blue: #0f4e7d;
    --card-blue-deep: #0b3a5e;
    --ink-white: #ffffff;
    --emboss: rgba(6, 40, 66, 0.45);
  }
  * { margin: 0; padding: 0; box-sizing: border-box; }
  html, body {
    width: 1200px;
    height: 900px;
    overflow: hidden;
    background: var(--backdrop);
    font-family: "Arimo", Arial, sans-serif;
  }
  .canvas {
    position: relative;
    width: 1200px;
    height: 900px;
  }
  .card {
    position: absolute;
    left: 320px;
    width: 560px;
    height: 320px;
    border-radius: 4px;
    box-shadow: 0 10px 26px rgba(0, 0, 0, 0.22);
    overflow: hidden;
    color: var(--ink-white);
  }
  .card-back {
    top: 100px;
    background: radial-gradient(circle at 50% 50%, var(--card-blue-light) 0%, var(--card-blue) 55%, var(--card-blue-deep) 100%);
    display: flex;
    align-items: center;
    justify-content: center;
  }
  .back-mark {
    display: flex;
    align-items: center;
    gap: 18px;
  }
  .back-mark-dot {
    width: 110px;
    height: 110px;
    border-radius: 50%;
    background: var(--emboss);
  }
  .back-mark-name {
    font-size: 40px;
    font-weight: 400;
    letter-spacing: 1px;
    color: var(--emboss);
  }
  .card-front {
    top: 480px;
    background: linear-gradient(135deg, var(--card-blue-light) 0%, var(--card-blue) 45%, var(--card-blue-deep) 100%);
    padding: 34px 0 0 48px;
  }
  .brand {
    display: flex;
    align-items: center;
    gap: 12px;
    margin-left: 70px;
  }
  .brand-dot {
    width: 54px;
    height: 54px;
    border-radius: 50%;
    background: var(--ink-white);
  }
  .brand-name {
    font-size: 30px;
    font-weight: 400;
    line-height: 1;
  }
  .brand-tagline {
    font-size: 11px;
    line-height: 1.2;
    text-align: right;
    margin-top: 3px;
  }
  .person {
    margin-top: 22px;
    margin-left: 18px;
  }
  .person-name {
    font-size: 22px;
    font-weight: 400;
    letter-spacing: 0.5px;
  }
  .person-title {
    font-size: 15px;
    margin-top: 2px;
  }
  .contact {
    margin-top: 14px;
    margin-left: 10px;
    font-size: 15px;
    line-height: 1.35;
  }
  .address {
    margin-top: 10px;
    margin-left: 4px;
    font-size: 15px;
  }
  .website {
    margin-top: 8px;
    font-size: 17px;
    font-weight: 700;
  }
</style>
</head>
<body>
<main class="canvas">
  <section class="card card-back" aria-label="Card back">
    <div class="back-mark">
      <span class="back-mark-dot"></span>
      <span class="back-mark-name">CRESTLINE</span>
    </div>
  </section>

  <section class="card card-front" aria-label="Card front">
    <div class="brand">
      <span class="brand-dot"></span>
      <div class="brand-text">
        <div class="brand-name">CRESTLINE</div>
        <div class="brand-tagline">Orthopaedic &amp; Sports<br>Medicine Center</div>
      </div>
    </div>
    <div class="person">
      <div class="person-name">WARREN DELANEY</div>
      <div class="person-title">CEO</div>
    </div>
    <div class="contact">
      <div class="phone">(318) 555-0142</div>
      <div class="email">wdelaney@crestlineortho.com</div>
    </div>
    <div class="address">1820 Harlow Ave., Pinewood, LA 71390</div>
    <div class="website">www.crestlineortho.com</div>
  </section>
</main>
</body>
</html>
```